Professional Coaching Business Letterhead/Footer

I need a letterhead and email footer for my personal coaching business, Dorian K Falstead Professional Coaching. I send several attachments to new clients (such as welcome letter, fee structure, etc) and would like these pages to have my branding on them.
I prefer the black and gold/silver color scheme, and will attach my logo to be used. I'd like the overall impression to be upmarket/regal/professional.

One of the uploaded files is my business card, to give an idea of the style/feel I like. The others are vector files containing logo to be used.

Target Market(s)

Corporate managers, successful business people. 30-60 yrs old.

Industry/Entity Type

Business

Requirements
Must have
• Logo (DKF)
Nice to have
• Shield emblem around logo, some type of watermark.
Should not have
• The first uploaded file is my business card, intended to show style and colors- not to be used itself as the letterhead.

```html
<!DOCTYPE html>
<html lang="en">
<head>
<meta charset="utf-8">
<title>Dorian K Falstead Professional Coaching – Letterhead</title>
<link rel="stylesheet" href="https://fonts.googleapis.com/css2?family=Questrial&display=swap">
<style>
  :root {
    --ink: #111111;
    --paper: #ffffff;
    --gold-deep: #f29a0e;
    --gold-bright: #ffd51c;
    --silver-light: #e4e4e4;
    --silver-mid: #b5b5b5;
    --silver-dark: #7d7d7d;
    --watermark: #e9e9e9;
    --shadow-grey: #d9d9d9;
  }
  html, body {
    margin: 0;
    padding: 0;
    width: 864px;
    height: 1200px;
    overflow: hidden;
    background: var(--paper);
  }
  .letterhead {
    position: relative;
    width: 864px;
    height: 1200px;
    background: var(--paper);
    font-family: "Questrial", "Helvetica Neue", Arial, sans-serif;
  }
  .decor {
    position: absolute;
    inset: 0;
    width: 864px;
    height: 1200px;
  }
  .brand-mark {
    position: absolute;
    left: 84px;
    top: 52px;
    width: 132px;
    height: 132px;
    border: 6px solid var(--ink);
    border-radius: 50%;
    box-sizing: border-box;
    display: flex;
    align-items: center;
    justify-content: center;
    color: var(--ink);
    font-size: 40px;
    letter-spacing: 1px;
  }
  .brand-name {
    position: absolute;
    left: 72px;
    top: 182px;
    margin: 0;
    font-size: 19px;
    font-weight: 400;
    letter-spacing: 0.5px;
    color: var(--ink);
    white-space: nowrap;
  }
  .watermark-initials {
    position: absolute;
    left: 283px;
    top: 408px;
    width: 310px;
    height: 310px;
    display: flex;
    align-items: center;
    justify-content: center;
    color: var(--watermark);
    font-size: 110px;
    letter-spacing: 4px;
  }
  .watermark-name {
    position: absolute;
    left: 0;
    width: 864px;
    top: 752px;
    margin: 0;
    text-align: center;
    font-size: 42px;
    font-weight: 400;
    letter-spacing: 2px;
    color: var(--watermark);
    white-space: nowrap;
  }
</style>
</head>
<body>
<main class="letterhead">
  <svg class="decor" viewBox="0 0 864 1200" xmlns="http://www.w3.org/2000/svg" aria-hidden="false">
    <defs>
      <linearGradient id="gold-sweep" x1="0" y1="0" x2="1" y2="0">
        <stop offset="0" stop-color="var(--gold-deep)"/>
        <stop offset="1" stop-color="var(--gold-bright)"/>
      </linearGradient>
      <linearGradient id="silver-sweep" x1="0" y1="0" x2="1" y2="0">
        <stop offset="0" stop-color="var(--silver-light)"/>
        <stop offset="0.6" stop-color="var(--silver-mid)"/>
        <stop offset="1" stop-color="var(--silver-dark)"/>
      </linearGradient>
      <linearGradient id="silver-base" x1="0" y1="0" x2="1" y2="0">
        <stop offset="0" stop-color="var(--silver-dark)"/>
        <stop offset="0.5" stop-color="var(--silver-mid)"/>
        <stop offset="1" stop-color="var(--silver-light)"/>
      </linearGradient>
      <linearGradient id="gold-base" x1="0" y1="0" x2="1" y2="0">
        <stop offset="0" stop-color="var(--gold-bright)"/>
        <stop offset="1" stop-color="var(--gold-deep)"/>
      </linearGradient>
      <linearGradient id="faint-flourish" x1="0" y1="0" x2="1" y2="0">
        <stop offset="0" stop-color="var(--watermark)" stop-opacity="0"/>
        <stop offset="0.5" stop-color="var(--watermark)"/>
        <stop offset="1" stop-color="var(--watermark)" stop-opacity="0"/>
      </linearGradient>
      <radialGradient id="gold-flourish" cx="0.5" cy="0.5" r="0.5">
        <stop offset="0" stop-color="var(--gold-deep)" stop-opacity="0.55"/>
        <stop offset="1" stop-color="var(--gold-bright)" stop-opacity="0"/>
      </radialGradient>
    </defs>

    <!-- header sweeps -->
    <path class="header-silver" fill="url(#silver-sweep)"
      d="M520 38 L825 38 L825 96 C770 80 690 72 610 76 C540 80 480 96 420 116 C470 80 520 52 600 38 Z"/>
    <path class="header-shadow" fill="var(--shadow-grey)"
      d="M200 168 C270 156 330 112 430 86 C520 64 600 58 680 62 C580 70 500 90 430 116 C330 150 280 178 210 180 Z"/>
    <path class="header-gold" fill="url(#gold-sweep)"
      d="M178 38 L720 38 C640 48 540 56 440 76 C340 98 280 150 212 162 C196 140 186 96 178 38 Z"/>
    <circle class="header-logo-ground" cx="150" cy="118" r="80" fill="var(--paper)"/>

    <!-- watermark -->
    <circle class="watermark-ring" cx="438" cy="563" r="152" fill="none" stroke="var(--watermark)" stroke-width="8"/>
    <rect class="watermark-flourish-left" role="img" aria-label="Faint decorative flourish" x="110" y="762" width="130" height="22" rx="11" fill="url(#faint-flourish)"/>
    <rect class="watermark-flourish-right" role="img" aria-label="Faint decorative flourish" x="630" y="762" width="130" height="22" rx="11" fill="url(#faint-flourish)"/>

    <!-- footer sweeps -->
    <path class="footer-gold" fill="url(#gold-base)"
      d="M39 1118 C70 1146 170 1156 300 1150 C420 1145 500 1130 580 1124 C480 1150 400 1166 300 1166 L39 1166 Z"/>
    <path class="footer-silver" fill="url(#silver-base)"
      d="M400 1166 C540 1148 680 1122 825 1138 L825 1166 Z"/>
    <path class="footer-black" fill="var(--ink)"
      d="M39 1100 C42 1042 96 1012 136 1024 C92 1022 62 1052 64 1088 C72 1128 170 1136 300 1128 C450 1118 560 1088 680 1092 C740 1095 790 1106 825 1120 L825 1132 C780 1118 730 1108 680 1110 C560 1114 450 1144 300 1150 C170 1155 62 1148 39 1122 Z"/>
    <ellipse class="footer-flourish" role="img" aria-label="Gold decorative flourish" cx="750" cy="1118" rx="72" ry="48" fill="url(#gold-flourish)"/>

    <!-- page frame -->
    <rect class="page-frame" x="39" y="37" width="786" height="1129" fill="none" stroke="var(--ink)" stroke-width="2"/>
  </svg>

  <div class="brand-mark">DKF</div>
  <p class="brand-name">DORIAN K FALSTEAD</p>

  <div class="watermark-initials">DKF</div>
  <p class="watermark-name">DORIAN K FALSTEAD</p>
</main>
</body>
</html>
```